Doors for Chiropractic Office

In my chiropractic office I have 6 treatment rooms and 2 massage rooms. The entire office is going through a remodel. The overall color scheme is very earth tones but in order to add some color, the 6 doors to the treatment rooms will all be a separate color (Red, Blue, Yellow, Green etc)
I need to number each room 1,2,3,4,5,6 and the 2 massage rooms. I had the idea of putting a giant number on each door, so I am looking for some graphic ideas for that project.
The rooms are located with 4 on each side of a long hallway with the 2 massage rooms at the end.
The purpose of numbering each door is to direct the patients where to go.
I have uploaded pictures of the hall way. Pardon the dust since we are under construction but hopefully it gives you an idea of the layout. The door colors will change as stated above.

Requirements
Nice to have
• I would like to see someone come up with a design where each number for the doors are created out of vertebrae's.

```html
<!DOCTYPE html>
<html lang="en">
<head>
<meta charset="utf-8">
<title>Treatment Room Door Numbers</title>
<link rel="stylesheet" href="https://fonts.googleapis.com/css2?family=Inter:wght@200;400&display=swap">
<style>
  :root {
    --bg: #f1f1ef;
    --door-red: #ad2d34;
    --door-yellow: #e0b417;
    --door-green: #13973d;
    --door-blue: #115a97;
    --ink: #f4f4f2;
  }
  html, body {
    margin: 0;
    padding: 0;
    width: 1200px;
    height: 1050px;
    overflow: hidden;
    background: var(--bg);
  }
  .door-set {
    position: relative;
    width: 1200px;
    height: 1050px;
  }
  .door {
    position: absolute;
    width: 165px;
    height: 349px;
    display: block;
  }
  .door--red    { fill: var(--door-red); }
  .door--yellow { fill: var(--door-yellow); }
  .door--green  { fill: var(--door-green); }
  .door--blue   { fill: var(--door-blue); }
  .numeral {
    fill: var(--ink);
    font-family: "Inter", sans-serif;
    font-weight: 200;
    font-size: 140px;
    text-anchor: middle;
  }
  .rule {
    stroke: var(--ink);
    stroke-width: 1.5;
  }
  .caption {
    fill: var(--ink);
    font-family: "Inter", sans-serif;
    font-weight: 400;
    font-size: 11px;
    letter-spacing: 2.5px;
    text-anchor: middle;
    text-transform: uppercase;
  }
</style>
</head>
<body>
<main class="door-set">
  <!-- Upper row -->
  <svg class="door door--red" style="left:184px; top:80px" viewBox="0 0 165 349" aria-label="Treatment room 1">
    <rect width="165" height="349"/>
    <text class="numeral" x="82.5" y="190">1</text>
    <line class="rule" x1="52" y1="212" x2="113" y2="212"/>
    <text class="caption" x="84" y="234">Room</text>
  </svg>
  <svg class="door door--yellow" style="left:400px; top:80px" viewBox="0 0 165 349" aria-label="Treatment room 2">
    <rect width="165" height="349"/>
    <text class="numeral" x="82.5" y="190">2</text>
    <line class="rule" x1="52" y1="212" x2="113" y2="212"/>
    <text class="caption" x="84" y="234">Room</text>
  </svg>
  <svg class="door door--green" style="left:623px; top:80px" viewBox="0 0 165 349" aria-label="Treatment room 3">
    <rect width="165" height="349"/>
    <text class="numeral" x="82.5" y="190">3</text>
    <line class="rule" x1="52" y1="212" x2="113" y2="212"/>
    <text class="caption" x="84" y="234">Room</text>
  </svg>
  <svg class="door door--blue" style="left:848px; top:80px" viewBox="0 0 165 349" aria-label="Massage room 1">
    <rect width="165" height="349"/>
    <text class="numeral" x="82.5" y="190">1</text>
    <line class="rule" x1="52" y1="212" x2="113" y2="212"/>
    <text class="caption" x="84" y="234">Massage</text>
  </svg>

  <!-- Lower row -->
  <svg class="door door--red" style="left:184px; top:612px" viewBox="0 0 165 349" aria-label="Treatment room 4">
    <rect width="165" height="349"/>
    <text class="numeral" x="82.5" y="190">4</text>
    <line class="rule" x1="52" y1="212" x2="113" y2="212"/>
    <text class="caption" x="84" y="234">Room</text>
  </svg>
  <svg class="door door--yellow" style="left:397px; top:612px" viewBox="0 0 165 349" aria-label="Treatment room 5">
    <rect width="165" height="349"/>
    <text class="numeral" x="82.5" y="190">5</text>
    <line class="rule" x1="52" y1="212" x2="113" y2="212"/>
    <text class="caption" x="84" y="234">Room</text>
  </svg>
  <svg class="door door--green" style="left:623px; top:612px" viewBox="0 0 165 349" aria-label="Treatment room 6">
    <rect width="165" height="349"/>
    <text class="numeral" x="82.5" y="190">6</text>
    <line class="rule" x1="52" y1="212" x2="113" y2="212"/>
    <text class="caption" x="84" y="234">Room</text>
  </svg>
  <svg class="door door--blue" style="left:849px; top:612px" viewBox="0 0 165 349" aria-label="Massage room 2">
    <rect width="165" height="349"/>
    <text class="numeral" x="82.5" y="190">2</text>
    <line class="rule" x1="52" y1="212" x2="113" y2="212"/>
    <text class="caption" x="84" y="234">Massage</text>
  </svg>
</main>
</body>
</html>
```